Business card design for Velvet Harbor

We need business cards designed for our new marketing consulting company, Velvet Harbor. Our services include marketing strategy, go-to-market and launch planning, growth strategy, and execution. We serve medical technology and health technology companies, from startups to well-established growth companies.

The business cards should feel professional, credible, reliable and trustworthy, and should instill confidence. Also bold, creative, and modern.

The design must use the Velvet Harbor logo.

The primary brand color is this orange: #FF5501
A secondary color that you can use is this gray: #282B2D
I would prefer only to use the orange and gray. But if you feel you really need an additional accent color (please use it very sparingly, as little as possible), you can use this blue for small accent purposes: #009FED

Attached are the logo files. The main logo is the one with a little bit of orange on the left and the rest is gray.

The business card should include the following:

Velvet Harbor logo
First name and last name
Title
Email address
Phone number and type (in whatever order looks best for the design
Website (the website does not need to be in the same block as the personal info)

For example:

Nessa Pryle
Founder & Principal
nessa@velvetharbor.com
+1.628.309.4156 mobile (can use "." or spaces in between blocks of numbers)
velvetharbor.com (somewhere on the card, it does not need to be with the personal info; and note that there is no "www." at the beginning)

Note that there will be no address listed on the business card.

Target Market(s)

Executives (CEO, head of marketing, head of sales) at medical technology and health technology companies, mostly in their 40s and older, well-educated, often with advanced degrees. They are strategic thinkers, responsible for budgets, and familiar with P&L. Their comfort with and trust in using outside consultants varies.

Industry/Entity Type

Medical technology and health technology companies.

Contact Information for Business Card

See project description

Font styles to use
Sans Serif

Requirements
Must have
• Logo and see Business card details section above.

```html
<!DOCTYPE html>
<html lang="en">
<head>
<meta charset="utf-8">
<title>Velvet Harbor — Business Card</title>
<link href="https://fonts.googleapis.com/css2?family=Montserrat:wght@400;500;700&display=swap" rel="stylesheet">
<style>
  :root {
    --orange: #FF5501;
    --orange-deep: #DC5020;
    --orange-light: #E9855F;
    --gray: #282B2D;
    --gray-light: #5E6062;
    --paper: #ECECEC;
    --white: #FFFFFF;
    --stage: #C9C9C9;
  }
  * { box-sizing: border-box; margin: 0; padding: 0; }
  html, body { width: 1200px; height: 1200px; overflow: hidden; }
  body {
    background: var(--stage);
    font-family: "Montserrat", sans-serif;
    position: relative;
  }
  .card {
    position: absolute;
    left: 150px;
    width: 900px;
    height: 514px;
    border-radius: 30px;
    overflow: hidden;
    box-shadow: 0 10px 30px rgba(0,0,0,0.18);
  }
  .card-back {
    top: 70px;
    background: linear-gradient(115deg, var(--gray-light) 0%, var(--gray) 60%);
  }
  .card-front { top: 616px; background: var(--orange-deep); }

  .brand {
    position: absolute;
    display: flex;
    align-items: center;
    gap: 22px;
  }
  .brand-dot { border-radius: 50%; background: var(--orange); flex: none; }
  .brand-name { font-weight: 700; letter-spacing: 0.08em; text-transform: uppercase; white-space: nowrap; }

  .card-back .brand { left: 0; right: 0; top: 0; bottom: 0; justify-content: center; }
  .card-back .brand-dot { width: 92px; height: 92px; }
  .card-back .brand-name { color: var(--white); font-size: 64px; }

  .front-art { position: absolute; inset: 0; width: 900px; height: 514px; }

  .card-front .brand { left: 590px; top: 210px; gap: 12px; }
  .card-front .brand-dot { width: 36px; height: 36px; }
  .card-front .brand-name { color: var(--gray); font-size: 22px; letter-spacing: 0.06em; }

  .holder { position: absolute; left: 70px; top: 62px; color: var(--white); }
  .holder-name { font-weight: 700; font-size: 44px; line-height: 1.1; }
  .holder-title { font-weight: 400; font-size: 22px; margin-top: 4px; margin-left: 18px; }

  .contacts {
    position: absolute; left: 110px; top: 392px;
    list-style: none; color: var(--white); font-size: 21px; font-weight: 500;
  }
  .contacts li { display: flex; align-items: center; gap: 14px; height: 32px; }
  .contacts svg { width: 20px; height: 20px; fill: var(--white); flex: none; }
</style>
</head>
<body>

<section class="card card-back">
  <div class="brand">
    <span class="brand-dot"></span>
    <span class="brand-name">Velvet Harbor</span>
  </div>
</section>

<section class="card card-front">
  <svg class="front-art" viewBox="0 0 900 514" aria-hidden="true">
    <defs>
      <linearGradient id="orangeFade" x1="0" y1="0" x2="1" y2="0">
        <stop offset="0" stop-color="var(--orange-light)"/>
        <stop offset="0.6" stop-color="var(--orange-deep)"/>
      </linearGradient>
    </defs>
    <rect width="900" height="514" fill="url(#orangeFade)"/>
    <path d="M470 0 C370 180 440 390 590 514 L900 514 L900 0 Z" fill="var(--white)"/>
    <path d="M478 0 C385 180 460 390 615 514 L900 514 L900 0 Z" fill="var(--gray)"/>
    <path d="M498 0 C420 170 500 380 660 514 L900 514 L900 0 Z" fill="var(--orange-deep)"/>
    <path d="M540 0 C450 150 490 360 690 514 L900 514 L900 0 Z" fill="var(--paper)"/>
  </svg>

  <div class="holder">
    <h1 class="holder-name">Nessa Pryle</h1>
    <p class="holder-title">Founder &amp; Principal</p>
  </div>

  <ul class="contacts">
    <li>
      <svg viewBox="0 0 24 24"><path d="M6.6 10.8a15.1 15.1 0 0 0 6.6 6.6l2.2-2.2a1 1 0 0 1 1-.25 11.4 11.4 0 0 0 3.6.57 1 1 0 0 1 1 1V20a1 1 0 0 1-1 1A17 17 0 0 1 3 4a1 1 0 0 1 1-1h3.5a1 1 0 0 1 1 1c0 1.25.2 2.450.57 3.570a1 1 0 0 1-.25 1z"/></svg>
      +1.628.309.4156
    </li>
    <li>
      <svg viewBox="0 0 24 24"><path d="M2 5h20v14H2z M3.5 6.5 12 12.5l8.5-6z" fill-rule="evenodd"/></svg>
      nessa@velvetharbor.com
    </li>
    <li>
      <svg viewBox="0 0 24 24"><path d="M12 2a10 10 0 1 0 0 20 10 10 0 0 0 0-20zm-1 2.1V11H4.1A8 8 0 0 1 11 4.1zm2 0A8 8 0 0 1 19.9 11H13zM4.1 13H11v6.9A8 8 0 0 1 4.1 13zm8.9 6.9V13h6.9a8 8 0 0 1-6.9 6.9z"/></svg>
      www.velvetharbor.com
    </li>
  </ul>

  <div class="brand">
    <span class="brand-dot"></span>
    <span class="brand-name">Velvet Harbor</span>
  </div>
</section>

</body>
</html>
```